COOL PROJECT: Modern and Elegant Design for a Luxury Home Cleaning Company

We're looking for an elegant car wrap design for a Home Cleaning company based in Miami called The Velora Maids. We clean homes for medium to wealthy people and we want to attract this audience.

The design should communicate trust, professionalism & expertise. While looking SEXY!

Specs:
- Car Model: Corvane Strada K Sport Trim 2021(I included a picture)
- Our Logo Font: Dosis Extra Bold(But if you have another cool font you want to test, we are open to other ideas)
- Please ensure to use the same colors as in the logo

Information to include on the car:
a. Slogan Options:
MORE THAN JUST A CLEANING
or
VELORA GLOW, DAY AFTER DAY

b. Our Website www.theveloramaidshq.co

c. (305) 555 - 0148

d. I also included a few stamp design files, feel free to use these if you think it could look cool somewhere(Files: Stamp 1, stamp 2, stamp 3)

HAVE FUN!

```html
<!DOCTYPE html>
<html lang="en">
<head>
<meta charset="utf-8">
<title>The Velora Maids — Vehicle Wrap Side Layout</title>
<link rel="stylesheet" href="https://fonts.googleapis.com/css2?family=Dosis:wght@600;700;800&display=swap">
<style>
  :root {
    --wrap-yellow: #f0b52c;
    --brand-navy: #183344;
    --gold-light: #f7d98a;
    --gold-mid: #e0ad3f;
    --gold-deep: #b98224;
    --page-bg: #ffffff;
  }
  html, body {
    margin: 0;
    padding: 0;
    width: 1200px;
    height: 1200px;
    overflow: hidden;
    background: var(--page-bg);
  }
  .canvas {
    position: relative;
    width: 1200px;
    height: 1200px;
  }
  .wrap-layout {
    position: absolute;
    left: 30px;
    top: 426px;
    width: 1140px;
    height: 348px;
    display: block;
  }
  .wrap-panel { fill: var(--wrap-yellow); }
  .brand-name {
    font-family: "Dosis", sans-serif;
    font-weight: 800;
    fill: var(--brand-navy);
  }
  .brand-mark { fill: var(--brand-navy); }
  .phone-number {
    font-family: "Dosis", sans-serif;
    font-weight: 700;
    fill: var(--brand-navy);
  }
  .website {
    font-family: "Dosis", sans-serif;
    font-weight: 600;
    fill: var(--brand-navy);
  }
  .slogan {
    font-family: "Dosis", sans-serif;
    font-weight: 800;
    fill: var(--brand-navy);
  }
  .stamp-ring { fill: url(#goldRing); }
  .stamp-core-navy { fill: var(--brand-navy); }
  .stamp-core-yellow { fill: var(--wrap-yellow); }
</style>
</head>
<body>
<main class="canvas">
  <svg class="wrap-layout" viewBox="0 0 1845 564" xmlns="http://www.w3.org/2000/svg" aria-label="The Velora Maids vehicle wrap, side layout">
    <defs>
      <radialGradient id="goldRing" cx="45%" cy="40%" r="65%">
        <stop offset="0%" stop-color="var(--gold-light)"/>
        <stop offset="60%" stop-color="var(--gold-mid)"/>
        <stop offset="100%" stop-color="var(--gold-deep)"/>
      </radialGradient>
    </defs>

    <rect class="wrap-panel" x="0" y="0" width="1845" height="564"/>

    <!-- front fender dot stamp -->
    <g class="stamp stamp-front-dot" role="img" aria-label="Small gold stamp seal">
      <circle class="stamp-ring" cx="45" cy="408" r="38"/>
      <circle class="stamp-core-navy" cx="45" cy="408" r="30"/>
    </g>

    <!-- front door small stamp -->
    <g class="stamp stamp-front" role="img" aria-label="Gold wax stamp seal">
      <circle class="stamp-ring" cx="328" cy="283" r="60"/>
      <circle class="stamp-core-yellow" cx="328" cy="283" r="46"/>
    </g>

    <!-- brand block -->
    <g class="brand-block">
      <rect class="brand-mark" x="504" y="318" width="52" height="52"/>
      <text class="brand-name" x="572" y="330" font-size="52">THE</text>
      <text class="brand-name" x="572" y="378" font-size="52">VELORA</text>
      <text class="brand-name" x="572" y="426" font-size="52">MAIDS</text>
      <text class="phone-number" x="506" y="487" font-size="46" textLength="324" lengthAdjust="spacingAndGlyphs">(305) 555 - 0148</text>
      <text class="website" x="509" y="532" font-size="30" textLength="338" lengthAdjust="spacingAndGlyphs">www.theveloramaidshq.co</text>
    </g>

    <!-- centre large stamp -->
    <g class="stamp stamp-centre" role="img" aria-label="Large gold wax stamp seal">
      <circle class="stamp-ring" cx="978" cy="403" r="114"/>
      <circle class="stamp-core-navy" cx="978" cy="403" r="88"/>
    </g>

    <!-- slogan -->
    <g class="slogan-block">
      <text class="slogan" x="1098" y="318" font-size="92" textLength="218" lengthAdjust="spacingAndGlyphs">VELORA</text>
      <text class="slogan" x="1106" y="392" font-size="80" textLength="208" lengthAdjust="spacingAndGlyphs">GLOW,</text>
      <text class="slogan" x="1114" y="456" font-size="62" textLength="202" lengthAdjust="spacingAndGlyphs">DAY AFTER</text>
      <text class="slogan" x="1126" y="540" font-size="86" textLength="170" lengthAdjust="spacingAndGlyphs">DAY</text>
    </g>

    <!-- rear quarter large stamp -->
    <g class="stamp stamp-rear" role="img" aria-label="Gold wax stamp seal">
      <circle class="stamp-ring" cx="1588" cy="240" r="104"/>
      <circle class="stamp-core-yellow" cx="1588" cy="240" r="84"/>
    </g>

    <!-- rear small stamp -->
    <g class="stamp stamp-rear-small" role="img" aria-label="Small gold wax stamp seal">
      <circle class="stamp-ring" cx="1770" cy="405" r="65"/>
      <circle class="stamp-core-yellow" cx="1770" cy="405" r="50"/>
    </g>
  </svg>
</main>
</body>
</html>
```